Updated DJ business Card showing other businesses

DJ Kestro offers professional mobile dj services including DJ. MC. Karaoke.
Silent Disco (will attach logo)
I also offer a 360 Photo Booth.

Contact info:
(555) 314-7720
lenny.corbitt@mailvane.net
Social Media @DJKestroBPZ

```html
<!DOCTYPE html>
<html lang="en">
<head>
<meta charset="utf-8">
<title>DJ Kestro Business Card</title>
<link rel="stylesheet" href="https://fonts.googleapis.com/css2?family=Anton&family=Montserrat:wght@600;700&display=swap">
<style>
  :root {
    --page: #2a2a2c;
    --card-light: #ffffff;
    --card-dark: #0d0d0e;
    --ink: #111111;
    --ink-soft: #2b2b2b;
    --accent: #d42a58;
    --paper: #ffffff;
    --shade: #262628;
  }
  * { margin: 0; padding: 0; box-sizing: border-box; }
  html, body { width: 1200px; height: 900px; overflow: hidden; background: var(--page); }
  .canvas {
    width: 1200px; height: 900px;
    display: flex; flex-direction: column; align-items: center; justify-content: center;
    gap: 40px;
  }
  .card {
    width: 680px; height: 389px; border-radius: 26px;
    position: relative; overflow: hidden;
    box-shadow: 0 14px 30px rgba(0,0,0,0.45);
  }

  /* Front */
  .card-front { background: var(--card-light); }
  .mascot-area {
    position: absolute; left: -40px; top: -20px; width: 360px; height: 430px;
    background: radial-gradient(ellipse 62% 58% at 45% 50%, var(--ink) 0%, #1c1c1c 55%, rgba(17,17,17,0.55) 78%, rgba(255,255,255,0) 100%);
    border-radius: 0 48% 48% 0;
  }
  .front-copy {
    position: absolute; left: 330px; top: 70px; width: 320px;
  }
  .brand-name {
    font-family: "Anton", sans-serif; font-size: 54px; line-height: 1;
    color: var(--accent); letter-spacing: 1px; text-transform: uppercase;
  }
  .service-line {
    font-family: "Anton", sans-serif; font-size: 30px; line-height: 1.1;
    color: var(--ink-soft); text-transform: uppercase; margin-top: 10px;
  }
  .service-list {
    font-family: "Montserrat", sans-serif; font-weight: 600; font-size: 21px;
    color: var(--accent); letter-spacing: 2px; margin-top: 10px; text-transform: uppercase;
  }
  .extra-services {
    display: flex; align-items: center; gap: 12px; margin-top: 18px;
  }
  .partner-badge {
    width: 46px; height: 46px; border-radius: 50%;
    background: var(--ink-soft); flex: none;
  }
  .extra-label {
    font-family: "Montserrat", sans-serif; font-weight: 700; font-size: 15px;
    color: var(--ink-soft); letter-spacing: 1.5px; text-transform: uppercase; line-height: 1.35;
  }

  /* Back */
  .card-back { background: linear-gradient(120deg, var(--card-dark) 0%, #1b1b1d 55%, var(--card-dark) 100%); }
  .back-shade {
    position: absolute; left: -60px; top: -20px; width: 330px; height: 430px;
    background: radial-gradient(ellipse 60% 58% at 40% 50%, var(--shade) 0%, rgba(38,38,40,0.6) 60%, rgba(38,38,40,0) 100%);
    border-radius: 0 48% 48% 0;
  }
  .back-copy { position: absolute; left: 190px; top: 58px; right: 40px; }
  .back-brand {
    font-family: "Anton", sans-serif; font-size: 92px; line-height: 1;
    color: var(--paper); text-transform: uppercase; letter-spacing: 2px;
  }
  .back-brand .brand-prefix { color: var(--paper); }
  .contact { margin-top: 30px; font-family: "Montserrat", sans-serif; color: var(--paper); }
  .contact-phone { display: flex; align-items: center; gap: 10px; font-weight: 700; font-size: 34px; letter-spacing: 1px; }
  .contact-phone svg { width: 26px; height: 26px; fill: var(--paper); }
  .contact-email { font-weight: 600; font-size: 19px; letter-spacing: 1px; margin-top: 8px; text-transform: uppercase; }
  .contact-social { font-weight: 600; font-size: 16px; letter-spacing: 1.5px; margin-top: 8px; text-transform: uppercase; }
</style>
</head>
<body>
<main class="canvas">
  <section class="card card-front">
    <div class="mascot-area" role="img" aria-label="Large brand mascot illustration in black"></div>
    <div class="front-copy">
      <div class="brand-name">DJ Kestro</div>
      <div class="service-line">Offers professional<br>mobile DJ services</div>
      <div class="service-list">DJ. MC. Karaoke</div>
      <div class="extra-services">
        <div class="partner-badge" role="img" aria-label="Silent disco service badge"></div>
        <div class="extra-label">Silent Disco<br>360 Photo Booth</div>
      </div>
    </div>
  </section>

  <section class="card card-back">
    <div class="back-shade" role="img" aria-label="Faint brand mascot decoration"></div>
    <div class="back-copy">
      <div class="back-brand">DJ Kestro</div>
      <div class="contact">
        <div class="contact-phone">
          <svg viewBox="0 0 24 24" aria-hidden="true"><path d="M6.6 10.8a15.1 15.1 0 0 0 6.6 6.6l2.2-2.2a1 1 0 0 1 1-.25 11.4 11.4 0 0 0 3.6.57 1 1 0 0 1 1 1V20a1 1 0 0 1-1 1A17 17 0 0 1 3 4a1 1 0 0 1 1-1h3.5a1 1 0 0 1 1 1c0 1.25.2 2.450.57 3.57a1 1 0 0 1-.25 1z"/></svg>
          (555) 314-7720
        </div>
        <div class="contact-email">lenny.corbitt@mailvane.net</div>
        <div class="contact-social">@DJKestroBPZ</div>
      </div>
    </div>
  </section>
</main>
</body>
</html>
```